Plakat-Design für Stellenanzeige für eine Allgemeinarztpraxis
Zielgruppe
Gemeinde Talbach, ein kleine Landgemeinde im Nordosten von Baden-Württemberg mit ca. 3.600 Einwohner sucht für die ortsansässige Allgemeinarztpraxis einen Nachfolger*in. Die optimale Zielgruppe wären ja junge Ärzte - da sich dies wahrscheinlich als schwierig erweist wird an keine spezielle Altersgruppe gedacht.
Aufgabenstellung
Für die Bewerbung soll ein Straßenbanner im Bauzaunformat (340 x 0173 cm) erstellt werden.
Der Slogan könnte: 'Talbach sucht einen Arzt' oder ähnlich lauten.
Ein modernes auffälliges Design wäre wünschenswert.

```html
<!DOCTYPE html>
<html lang="de">
<head>
<meta charset="utf-8">
<title>Heldenarzt gesucht – Straßenbanner</title>
<link href="https://fonts.googleapis.com/css2?family=Raleway:ital,wght@1,700;1,800;1,900&display=swap" rel="stylesheet">
<style>
  :root {
    --stage: #dcdcdc;
    --banner: #f3f3f4;
    --brand-blue: #1565b0;
    --ink: #111111;
    --white: #ffffff;
    --photo-light: #eef2f7;
    --photo-mid: #b9cde3;
  }
  * { margin: 0; padding: 0; box-sizing: border-box; }
  html, body {
    width: 1200px; height: 864px; overflow: hidden;
    background: var(--stage);
  }
  .banner {
    position: absolute; left: 0; top: 132px;
    width: 1200px; height: 600px;
    background: var(--banner);
    font-family: "Raleway", sans-serif;
    font-style: italic;
  }
  .team-photo {
    position: absolute; left: 49px; top: 85px;
    width: 566px; height: 440px;
    background: radial-gradient(ellipse at 55% 45%, var(--photo-mid) 0%, var(--photo-light) 62%, var(--banner) 80%);
    border-radius: 40px;
  }
  .headline {
    position: absolute; left: 600px; width: 560px;
    text-align: center; color: var(--brand-blue);
    font-weight: 800; font-size: 78px; line-height: 1;
    letter-spacing: -1px;
  }
  .headline--town { top: 62px; }
  .headline--verb { top: 156px; }
  .highlight-box {
    position: absolute; left: 600px; top: 262px;
    width: 552px; height: 124px;
    background: var(--brand-blue);
    transform: rotate(-1deg);
    display: flex; align-items: center; justify-content: center;
  }
  .highlight-box__text {
    color: var(--white); font-weight: 900; font-size: 92px;
    letter-spacing: -1px; line-height: 1;
  }
  .apply-note {
    position: absolute; left: 600px; top: 434px; width: 560px;
    text-align: center; color: var(--ink);
    font-weight: 700; font-size: 33px;
  }
  .apply-url {
    position: absolute; left: 600px; top: 486px; width: 560px;
    text-align: center; color: var(--brand-blue);
    font-weight: 700; font-size: 30px;
  }
</style>
</head>
<body>
  <section class="banner">
    <div class="team-photo" role="img" aria-label="Gruppe von Ärztinnen, Ärzten und Pflegekräften in Schutzkleidung mit Masken und blauen Handschuhen"></div>
    <h1 class="headline headline--town">Talbach</h1>
    <p class="headline headline--verb">sucht einen</p>
    <div class="highlight-box"><span class="highlight-box__text">Heldenarzt!</span></div>
    <p class="apply-note">infos und bewerben unter:</p>
    <p class="apply-url">www.landgemeinde-talbach.de</p>
  </section>
</body>
</html>
```